Business Card Design Project - bel soravin group

dear Sirs

we need business card design for our group ( BEL Soravin Group ) , i have got the Logo design of our group from pixel harbor in previous , so all need details relating to our group i think available with you, as well as the the chosen logo design

we hope to provide us with business card logo that to be appropaite and satisfactory to us .

thanks

note : logo design of our group is attached .
Updates

Reason: please extend the deadline of my project for additional 15 days because i didn't received appropriate design for our gruop yet . kindly beaware that i have received 77 design till now , supossed to send me 200-250 design at least . thanks

Target Market(s)

contents
-

name : Korvan EL Mistrani

position : Operation Manager

Industry/Entity Type

Business

Requirements
Must have

• person name

group logo
Nice to have
• logo color matching with back background

```html
<!DOCTYPE html>
<html lang="en">
<head>
<meta charset="utf-8">
<title>BEL Soravin Group – Business Card</title>
<link rel="stylesheet" href="https://fonts.googleapis.com/css2?family=Open+Sans:ital,wght@0,400;0,600;0,700;1,400&display=swap">
<style>
  :root {
    --stage: #8a8a8a;
    --brand-blue: #1f5ea8;
    --brand-blue-dark: #174a88;
    --brand-blue-light: #2a78c4;
    --band-black: #1e1e1f;
    --paper: #f4f4f4;
    --ink: #2a2a2a;
    --white: #ffffff;
  }
  * { box-sizing: border-box; margin: 0; padding: 0; }
  html, body {
    width: 1200px; height: 880px; overflow: hidden;
    background: var(--stage);
    font-family: "Open Sans", Arial, sans-serif;
  }
  .canvas {
    width: 1200px; height: 880px;
    display: flex; flex-direction: column;
    align-items: center; justify-content: center; gap: 36px;
  }
  .card {
    position: relative; width: 700px; height: 400px; overflow: hidden;
    box-shadow: 0 6px 18px rgba(0,0,0,.25);
  }

  /* Front */
  .card--front {
    background: radial-gradient(ellipse at 45% 40%, var(--brand-blue-light) 0%, var(--brand-blue) 55%, var(--brand-blue-dark) 100%);
    color: var(--white);
  }
  .front-brand {
    position: absolute; left: 0; right: 0; top: 130px;
    display: flex; align-items: center; justify-content: center; gap: 16px;
  }
  .brand-mark { width: 26px; height: 26px; background: var(--white); }
  .front-brand .brand-name {
    font-size: 52px; font-weight: 600; letter-spacing: 1px; color: var(--white);
  }
  .front-web {
    position: absolute; left: 0; right: 0; top: 262px; text-align: center;
    font-size: 22px; font-style: italic; color: #e8eef7;
  }

  /* Back */
  .card--back { background: var(--paper); color: var(--ink); }
  .back-brand {
    position: absolute; left: 110px; top: 38px;
    display: flex; align-items: center; gap: 12px;
  }
  .back-brand .brand-mark { width: 20px; height: 20px; background: var(--brand-blue); }
  .back-brand .brand-name {
    font-size: 38px; font-weight: 600; color: var(--brand-blue);
  }
  .contact-list {
    position: absolute; left: 90px; top: 128px; list-style: none;
    font-size: 17px; line-height: 25px; color: var(--ink);
  }
  .contact-list li { display: flex; align-items: center; gap: 10px; }
  .contact-list svg { width: 15px; height: 15px; fill: var(--brand-blue-dark); flex: none; }
  .holder {
    position: absolute; right: 60px; top: 178px; text-align: right;
  }
  .holder-name {
    font-size: 28px; font-weight: 700; color: var(--brand-blue); line-height: 1.2;
  }
  .holder-role { font-size: 19px; color: var(--ink); }
  .footer-bands { position: absolute; left: 0; bottom: 0; width: 700px; height: 100px; }
  .address {
    position: absolute; left: 26px; bottom: 56px;
    font-size: 17px; color: #eaeaea;
  }
  .back-web {
    position: absolute; right: 32px; bottom: 10px;
    font-size: 22px; color: var(--white);
  }
</style>
</head>
<body>
<main class="canvas">

  <section class="card card--front" aria-label="Business card front">
    <div class="front-brand">
      <span class="brand-mark"></span>
      <span class="brand-name">BEL Soravin Group</span>
    </div>
    <p class="front-web">www.belsoravin.com</p>
  </section>

  <section class="card card--back" aria-label="Business card back">
    <div class="back-brand">
      <span class="brand-mark"></span>
      <span class="brand-name">BEL Soravin Group</span>
    </div>

    <ul class="contact-list">
      <li><svg viewBox="0 0 16 16"><path d="M3 2h3l1 4-2 1a9 9 0 0 0 4 4l1-2 4 1v3a1 1 0 0 1-1 1A12 12 0 0 1 2 3a1 1 0 0 1 1-1z"/></svg>+1 555 204 3187</li>
      <li><svg viewBox="0 0 16 16"><rect x="2" y="5" width="12" height="9" rx="1"/><rect x="4" y="2" width="8" height="4" fill="#1f5ea8"/></svg>+1 555 204 3190</li>
      <li><svg viewBox="0 0 16 16"><rect x="4" y="1" width="8" height="14" rx="1.5"/></svg>+1 555 718 6642</li>
      <li><svg viewBox="0 0 16 16"><rect x="1" y="3" width="14" height="10" rx="1"/><path d="M1.5 4l6.5 5 6.5-5" stroke="#f4f4f4" stroke-width="1.3" fill="none"/></svg>korvan@belsoravin.com</li>
    </ul>

    <div class="holder">
      <p class="holder-name">Korvan EL Mistrani</p>
      <p class="holder-role">Operation Manager</p>
    </div>

    <svg class="footer-bands" viewBox="0 0 700 100" preserveAspectRatio="none" aria-hidden="true">
      <rect x="0" y="46" width="700" height="54" fill="var(--brand-blue)"/>
      <path d="M0 0 H410 L440 46 H0 Z" fill="var(--band-black)"/>
      <path d="M440 46 H700 V50 H442 Z" fill="var(--band-black)"/>
    </svg>
    <p class="address">P.O.BOX 4821 Northgate, CN 5530</p>
    <p class="back-web">www.belsoravin.com</p>
  </section>

</main>
</body>
</html>
```